Fantasy Book Cover for 2nd Book in Ongoing Series

I need a full wrap design for the second book in my fantasy series. I've attached the cover for the first book. I'd like the same font and title style (color can be different) but the rest is open to change as long as it's obvious the books are part of the same series.

Title - Tides of Ashfall
Subtitle - A Novel of the Vestomari Lands
Title/Subtitle Font - Ringbearer
Author - Marguerite Calloway
Author/Blurb Font - Gadugi
Trim Size - 5.5 x 8.5
Pages - 410

Blurb -
Things have gone well for Orlane since her brother reclaimed Ombreval and freed their people: Bremon is becoming a stronger king each day, Halvue has found a home in the castle and its gardens, reports keep pouring in about peace within the lands. So why does Orlane feel antsy, as though something is missing?

When the neighboring king invites Orlane and Bremon to Venhol to rekindle relations and celebrate his birthday, Orlane jumps at the chance to travel again—and search for Dov, who’s still tracking Morvan Quell before the former prince can threaten Ombreval’s hard-won peace.

Venhol proves to be a pleasant realm, and Orlane and her friends settle in, until Bremon’s sanity begins to falter, and murder attempts on a Venholan noble shift to include Orlane and her brother.

With limited options, Orlane and her companions join forces with a Surim warrior and the Venholan princess to protect their loved ones. The farther they run for safety, the more the dangers envelope them and Bremon's grip on reality splinters. How can Orlane save her brother from his own mind?

Basics -
The setting for the story is traditional medieval based fantasy world - tunic/jerkin, boots, cloaks, swords, castles, magic, horses, wooden/stone houses, etc.
The first book mainly took place in the forests, hence the trees. The second is during the summer and moves into a capital city for a large portion of the book, then onto a large wooden ship that is taken over by pirates, then onto an isolated island where the characters are hunted by soldiers and battle them as well as a hurricane. So anything pertaining to any of that is acceptable.
The main storyline is about Orlane trying to help her brother, who's targeted for assassination and battling insanity, which is the result of a voodoo style magic be done on him by a rival, though the characters don't learn that until close to the end. Until then, he thinks he's being haunted by a malevolent person from his past.

I'm open to ideas both with and without the main character on the cover. If you have a design that includes the character, I would like either different images of the same woman, or a woman who at least looks a lot like her, or the picture done in a way that obscures or hides her features enough that you can't tell it's not the same woman. I don't want to use the same image as the first book cover though.

I've finally tracked down more images of the woman on book one, but note, in the one picture she has elf ears and my character is not an elf, so that would need changed. Hopefully this link works.
https://pixlink.io/82hQwTu

Target Market(s)

Adult fantasy readers, I have a roughly 60/40 split on female/male readership

Font styles to use
Other font styles liked:
• Ringbearer for title/subtitle, Gadugi for author/blurb

Requirements
Must have
• Ringbearer font for title and subtitle
Gadugi font for author and blurb
Traditional fantasy world feel - similar to Middle Earth or Westeros in buildings, clothing, traveling, etc.
Nice to have
• sense of adventure
since the last book had a relatively dark cover, I'd like this one a little lighter (but not bright)
Should not have
• While I have a lot of sexual tension in the books, I don't want scantily clad women on the cover. My strong female lead wears a full set of clothes.

```html
<!DOCTYPE html>
<html lang="en">
<head>
<meta charset="utf-8">
<title>Tides of Ashfall – Full Wrap Cover</title>
<link rel="stylesheet" href="https://fonts.googleapis.com/css2?family=Almendra+SC&family=Noto+Sans:wght@400&display=swap">
<style>
  :root {
    --page-bg: #ffffff;
    --cover-dark: #0d0f12;
    --cover-mid: #23272c;
    --castle-tone: #3a3f45;
    --cloak-teal: #16343f;
    --cloak-deep: #0b1a22;
    --skin-warm: #7a5544;
    --title-gold: #dca21a;
    --text-light: #f2f2f2;
    --spine-edge: rgba(0, 0, 0, 0.35);
  }
  * { margin: 0; padding: 0; box-sizing: border-box; }
  html, body {
    width: 1200px;
    height: 1200px;
    overflow: hidden;
    background: var(--page-bg);
  }
  .canvas {
    position: relative;
    width: 1200px;
    height: 1200px;
  }
  .wrap-cover {
    position: absolute;
    left: 50px;
    top: 204px;
    width: 1124px;
    height: 809px;
    transform: scale(0.9786);
    transform-origin: top left;
    background: var(--cover-dark);
    overflow: hidden;
  }
  .backdrop-scene {
    position: absolute;
    inset: 0;
    background:
      radial-gradient(ellipse 40% 55% at 58% 45%, var(--castle-tone) 0%, rgba(58,63,69,0.4) 45%, transparent 75%),
      linear-gradient(180deg, var(--cover-mid) 0%, #181b1f 55%, var(--cover-dark) 100%);
  }
  .heroine-art {
    position: absolute;
    left: 620px;
    top: 360px;
    width: 504px;
    height: 449px;
    background:
      radial-gradient(ellipse 18% 24% at 42% 30%, var(--skin-warm) 0%, rgba(122,85,68,0.5) 55%, transparent 80%),
      radial-gradient(ellipse 60% 70% at 45% 55%, var(--cloak-teal) 0%, var(--cloak-deep) 60%, transparent 100%);
  }
  .spine {
    position: absolute;
    left: 526px;
    top: 0;
    width: 70px;
    height: 809px;
    box-shadow: inset 6px 0 10px var(--spine-edge), inset -6px 0 10px var(--spine-edge);
  }
  .spine-title, .spine-author {
    position: absolute;
    left: 50%;
    writing-mode: vertical-rl;
    transform: translateX(-50%);
    white-space: nowrap;
  }
  .spine-title {
    top: 64px;
    font-family: "Almendra SC", serif;
    font-size: 40px;
    color: var(--title-gold);
    letter-spacing: -1px;
  }
  .spine-author {
    top: 522px;
    font-family: "Noto Sans", sans-serif;
    font-size: 20px;
    color: var(--text-light);
  }
  .back-cover {
    position: absolute;
    left: 90px;
    top: 60px;
    width: 400px;
  }
  .back-title {
    font-family: "Almendra SC", serif;
    font-weight: 400;
    font-size: 40px;
    line-height: 1;
    color: var(--title-gold);
    letter-spacing: -1px;
    margin-bottom: 12px;
  }
  .blurb p {
    font-family: "Noto Sans", sans-serif;
    font-size: 14.2px;
    line-height: 19.3px;
    color: var(--text-light);
    margin-bottom: 19px;
  }
  .front-title {
    position: absolute;
    left: 650px;
    top: 58px;
    width: 430px;
    text-align: center;
    font-family: "Almendra SC", serif;
    font-weight: 400;
    color: var(--title-gold);
  }
  .front-title .title-line {
    display: block;
    font-size: 96px;
    line-height: 92px;
    letter-spacing: -3px;
  }
  .front-subtitle {
    position: absolute;
    left: 650px;
    top: 244px;
    width: 430px;
    text-align: center;
    font-family: "Almendra SC", serif;
    font-size: 25px;
    color: var(--text-light);
    letter-spacing: -1px;
    white-space: nowrap;
  }
  .front-author {
    position: absolute;
    left: 650px;
    top: 728px;
    width: 460px;
    text-align: center;
    font-family: "Noto Sans", sans-serif;
    font-size: 27px;
    color: var(--text-light);
  }
</style>
</head>
<body>
  <main class="canvas">
    <section class="wrap-cover">
      <div class="backdrop-scene" role="img" aria-label="Dusky stone castle with turrets under a dark sky, spanning the back and front cover"></div>
      <div class="heroine-art" role="img" aria-label="Woman in a dark teal hooded cloak with a silver circlet, looking over her shoulder"></div>

      <article class="back-cover">
        <h2 class="back-title">Tides of Ashfall</h2>
        <div class="blurb">
          <p>Things have gone well for Orlane since her brother reclaimed Ombreval and freed their people: Bremon is becoming a stronger king each day, Halvue has found a home in the castle and its gardens, reports keep pouring in about peace within the lands. So why does Orlane feel antsy, as though something is missing?</p>
          <p>When the neighboring king invites Orlane and Bremon to Venhol to rekindle relations and celebrate his birthday, Orlane jumps at the chance to travel again—and search for Dov, who’s still tracking Morvan Quell before the former prince can threaten Ombreval’s hard-won peace.</p>
          <p>Venhol proves to be a pleasant realm, and Orlane and her friends settle in, until Bremon’s sanity begins to falter, and murder attempts on a Venholan noble shift to include Orlane and her brother.</p>
          <p>With limited options, Orlane and her companions join forces with a Surim warrior and the Venholan princess to protect their loved ones. The farther they run for safety, the more the dangers envelope them and Bremon's grip on reality splinters. How can Orlane save her brother from his own mind?</p>
        </div>
      </article>

      <div class="spine">
        <span class="spine-title">Tides of Ashfall</span>
        <span class="spine-author">Marguerite Calloway</span>
      </div>

      <h1 class="front-title">
        <span class="title-line">Tides of</span>
        <span class="title-line">Ashfall</span>
      </h1>
      <p class="front-subtitle">A Novel of the Vestomari Lands</p>
      <p class="front-author">Marguerite Calloway</p>
    </section>
  </main>
</body>
</html>
```